Adventurous female pilot

I am looking for a personal business card, for a very well qualified female pilot, with a lot of aviation experience.

Currently an airline pilot, have worked as a bush pilot in Africa, looking to get into corporate aviation, or private jet owners.
Want a classy looking card for networking...

Could be interested in a retro\vintage look also?!

An idea,, is an african sunset background, with my wings\logo on it
Updates

I just want to say thank you to all of your for your amazing designs!

I have been very busy flying this past week , so not had a chance to be on the computer much.
But I provide some feedback, and conclusions very soon!
Thank you again.

Marla

Reason: Still waiting on a couple of revisions to be 100% about my choice!

Target Market(s)

corporate aviation, private jet owners, casino's,
General audience.
networking

Industry/Entity Type

Airline

Requirements
Nice to have
• Classy, edgy, sexy, but also feminine

```html
<!DOCTYPE html>
<html lang="en">
<head>
<meta charset="utf-8">
<title>Marla Sorell – Business Card</title>
<link rel="stylesheet" href="https://fonts.googleapis.com/css2?family=Advent+Pro:wght@200&family=Jost:wght@400;500&display=swap">
<style>
  :root {
    --backdrop: #2e2e2e;
    --card: #f5f5f5;
    --ink: #555555;
    --ink-soft: #666666;
    --rule: #777777;
  }
  html, body {
    margin: 0;
    width: 1200px;
    height: 795px;
    overflow: hidden;
    background: var(--backdrop);
  }
  .stage {
    position: relative;
    width: 1200px;
    height: 795px;
    display: flex;
    align-items: center;
    justify-content: center;
  }
  .business-card {
    position: relative;
    width: 900px;
    height: 514px;
    background: var(--card);
    box-sizing: border-box;
  }
  .card-name {
    position: absolute;
    left: 130px;
    top: 130px;
    margin: 0;
    font-family: "Advent Pro", "Arial Narrow", sans-serif;
    font-weight: 200;
    font-size: 80px;
    letter-spacing: 9px;
    line-height: 1;
    color: var(--ink);
    text-transform: uppercase;
    white-space: nowrap;
  }
  .name-rule {
    position: absolute;
    left: 110px;
    top: 245px;
    width: 570px;
    height: 2px;
    background: var(--rule);
  }
  .contact-list {
    position: absolute;
    left: 0;
    top: 282px;
    margin: 0;
    display: grid;
    grid-template-columns: 300px auto;
    column-gap: 16px;
    row-gap: 4px;
    align-items: baseline;
    font-family: "Jost", "Futura", sans-serif;
    color: var(--ink);
  }
  .contact-label {
    text-align: right;
    font-size: 15px;
    font-weight: 500;
    letter-spacing: 0.5px;
    color: var(--ink-soft);
    text-transform: uppercase;
  }
  .contact-value {
    margin: 0;
    font-size: 25px;
    font-weight: 400;
    letter-spacing: 1px;
    text-transform: uppercase;
  }
</style>
</head>
<body>
  <main class="stage">
    <article class="business-card">
      <h1 class="card-name">Marla&nbsp;&nbsp;Sorell</h1>
      <div class="name-rule"></div>
      <dl class="contact-list">
        <dt class="contact-label">Cell U.S:</dt>
        <dd class="contact-value">+1 555-014-2298</dd>
        <dt class="contact-label">Cell Taipei:</dt>
        <dd class="contact-value">+886 900-555-123</dd>
        <dt class="contact-label">Email:</dt>
        <dd class="contact-value">marlasorell@skymail.com</dd>
      </dl>
    </article>
  </main>
</body>
</html>
```